Stand up pouch design for dog treats seafood & pasture themed (logo supplied)

We require a universal packaging design (front and back only) that can be used for multiple products across our range of dog treats.
Our company specialises in making air-dried, natural treats for dogs. Our product range includes seafood (sardines, whitebait, mussels) and meat products (liver, heart, kidney).
The packaging is to be used on stand up pouches such as these:
https://pouchworkshop.example.com.au/product/upright-bags-70g/
I currently do not have a template, however, you can assume the size will be similar to the one mentioned above (height 170, width 110). I will ask the printers to modify the design to fit into their templates when we are ready to print.
The design will need to be scalable to 150g and 250g bags, however, I don't think that will be a major issue as that is kept in mind as everything can just be enlarged.
The design will need to have a clear window at the front, similar to the koru picture here:
https://www.hounddepot.example.com.au/hounddepot-assets/images/products/p/koru-ridge-dry-dog-food-lamb.png
The clear window shouldn't be too large similar to how the koru one is quite small, as we need the bag to be opaque to protect the protein inside.
Our photoshop files for the logo are attached for reference in terms of style and colours.
The packaging should allow changing of the picture in the background on the front of the packaging to correspond with the type of protein that is being sold.
For example, the koru one has lamb in the back for lamb products, we would like to do the same.
We will require 4 background images that can be changed depending on the protein - sardines, NZ green lip mussels, whitebait, pasture with cows (this is for organ meats)
The back of the packaging should have a number of panels for us to place text, the design on the back can be static (no changing of the picture to correspond with protein type).
The placeholder text for the front and back of the package can be found here for each type (can just use 1 as placeholder example for design of the back):
https://barneysnacko.example.com.au/shop/premium-australian-caught-whitebait-dog-treats/
https://barneysnacko.example.com.au/shop/premium-australian-grass-fed-beef-heart-dog-treats/
https://barneysnacko.example.com.au/shop/premium-australian-caught-sardine-dog-treats/
https://barneysnacko.example.com.au/shop/premium-new-zealand-green-lip-mussel-dog-treats/
https://barneysnacko.example.com.au/shop/premium-australian-grass-fed-beef-kidney-dog-treats/
https://barneysnacko.example.com.au/shop/premium-australian-grass-fed-beef-liver-dog-treats/
For each product, we also have some icons and text (air-dried, single ingredient, etc) that we would like to have on the back of the bag. The icons and text can be found on the placeholder text mentioned above (example screenshot is attached).
Please also include weight in grams on the front.
The feel of the packaging should be clean, healthy and natural using the tones that are similar to our logo.
I've attached the packaging example that we like from koru, please do not copy the exact feel of the design in terms of colour or shape as we do not want too look too similar to that brand.
What we require:
1. Front design
2. Back design
3. 6 rendered images (of each product, with different backgrounds) of the front design on pouches that we can use on the website as product images.
Target Market(s)
Dog owners/lovers who want to purchase premium treats for their dogs
Industry/Entity Type
Dog treats

```html
<!DOCTYPE html>
<html lang="en">
<head>
<meta charset="utf-8">
<title>Barney's Snacko – Premium Natural Treats Pouches</title>
<link rel="stylesheet" href="https://fonts.googleapis.com/css2?family=Fredoka:wght@400;500;600;700&family=Josefin+Sans:wght@400;600&family=Oswald:wght@600&family=Open+Sans:wght@400;600;700&display=swap">
<style>
:root{
  --bg:#f4f4f4;
  --green:#1f8a45;
  --green-light:#2fb35e;
  --green-dark:#156b33;
  --orange:#ea8a3e;
  --white:#ffffff;
  --ink:#2a2a2a;
}
*{box-sizing:border-box;margin:0;padding:0}
html,body{width:1200px;height:615px;overflow:hidden;background:var(--bg)}
.canvas{position:relative;width:1200px;height:615px}
.pouch{position:absolute;top:97px;width:251px;height:411px;overflow:hidden;background:var(--green)}
.pouch--liver{left:32px}
.pouch--heart{left:338px}
.pouch--kidney{left:631px}
.pouch--back{left:927px;width:245px;background:linear-gradient(#f7f7f7,#e6e6e6)}

.scene{position:absolute;inset:0}
.pouch--liver .scene{background:linear-gradient(160deg,#4d7a45 0%,#6c8c6a 35%,#8aa3b1 60%,#3f6a3a 100%)}
.pouch--heart .scene{background:linear-gradient(170deg,#9cbfd8 0%,#d8e6ee 30%,#bcd3de 55%,#2d8a66 100%)}
.pouch--kidney .scene{background:linear-gradient(170deg,#b7cddd 0%,#6f9467 35%,#3d6e3c 60%,#2a7a3c 100%)}
.pasture{position:absolute;inset:0;clip-path:polygon(0 34%,68% 42%,100% 42%,100% 100%,0 100%);
  background:linear-gradient(180deg,rgba(31,138,69,.92),rgba(40,140,70,.85) 60%,rgba(30,120,55,.95))}
.pouch--heart .pasture{background:linear-gradient(180deg,rgba(30,140,110,.88),rgba(31,138,69,.9) 55%,rgba(30,120,55,.95))}

.tab{position:absolute;top:0;left:35px;width:180px;height:46px;border-radius:0 0 90px 90px/0 0 40px 40px;
  background:linear-gradient(var(--green-light),var(--green));color:var(--white);text-align:center;padding-top:10px}
.tab__title{font:500 18px/1 "Fredoka",sans-serif;letter-spacing:1px}
.tab__sub{font:600 6.5px/1.3 "Open Sans",sans-serif;letter-spacing:.2px}

.brand-panel{position:absolute;left:84px;top:46px;width:81px;height:120px;background:var(--white);
  display:flex;flex-direction:column;align-items:center;justify-content:center;gap:6px}
.brand-panel__dot{width:30px;height:30px;border-radius:50%;background:var(--orange)}
.brand-panel__name{font:700 11px/1.1 "Fredoka",sans-serif;color:var(--orange);text-align:center}

.origin-badge{position:absolute;left:186px;top:76px;width:54px;height:54px;border-radius:50%;
  background:radial-gradient(rgba(255,255,255,.55),rgba(255,255,255,.15))}
.dog-photo{position:absolute;left:140px;top:153px;width:111px;height:258px;
  background:linear-gradient(160deg,#8a5a33 0%,#e9e4dc 35%,#f6f4f0 70%,#ddd8cf 100%)}

.product-name{position:absolute;left:30px;top:208px;color:var(--white)}
.product-name__kind{font:400 22px/1 "Fredoka",sans-serif;letter-spacing:2px}
.product-name__type{font:700 31px/1 "Fredoka",sans-serif;color:var(--orange);letter-spacing:.5px}
.product-name__method{font:400 7.5px/1 "Josefin Sans",sans-serif;letter-spacing:1.2px;margin:3px 0 0 5px}
.divider{position:absolute;left:12px;top:275px;width:158px;height:1px;background:rgba(255,255,255,.8)}

.window{position:absolute;left:31px;top:305px;width:80px;height:52px;border:2px solid var(--white);border-top-width:3px;
  border-radius:0 0 40px 40px/0 0 34px 34px;background:linear-gradient(#c58a45,#a86a2e)}
.weight-tag{position:absolute;left:52px;top:352px;width:38px;height:20px;background:var(--white);border-radius:3px;
  text-align:center;color:var(--orange);padding-top:2px}
.weight-tag__label{font:400 3.8px/1 "Open Sans",sans-serif;letter-spacing:.3px}
.weight-tag__value{font:600 10px/1.2 "Fredoka",sans-serif}
.claims{position:absolute;left:123px;top:313px;display:flex;flex-direction:column;gap:5px}
.claims__badge{width:18px;height:18px;border-radius:50%;border:1px solid var(--white)}
.origin-line{position:absolute;left:48px;top:388px;font:700 4.5px/1 "Oswald",sans-serif;color:var(--white)}

/* back */
.back-heading{position:absolute;right:8px;top:77px;font:400 11px/1 "Josefin Sans",sans-serif;color:var(--green)}
.story-band{position:absolute;left:0;top:92px;width:100%;height:33px;background:var(--green);color:var(--white);
  font:700 3.9px/1.45 "Open Sans",sans-serif;text-transform:uppercase;text-align:center;padding:4px 10px 0;letter-spacing:.2px}
.promise-column{position:absolute;left:2px;top:129px;width:102px;height:282px;background:var(--green);color:var(--white);
  padding:9px 8px 0;text-align:center}
.promise{margin-bottom:11px}
.promise__no{font:600 8px/1 "Oswald",sans-serif;letter-spacing:1px}
.promise__title{font:600 4.8px/1.3 "Oswald",sans-serif;text-transform:uppercase;margin:2px 0}
.promise__text{font:400 4.4px/1.4 "Open Sans",sans-serif;text-align:justify}
.contact{border-top:1px solid rgba(255,255,255,.7);padding-top:3px;text-align:left;font:400 4px/1.5 "Open Sans",sans-serif}
.contact__item{display:flex;align-items:center;gap:2px}
.contact__item::before{content:"";width:3px;height:3px;border-radius:50%;background:var(--white)}
.info-column{position:absolute;left:111px;top:130px;width:128px;color:var(--ink);text-align:center}
.info{margin-bottom:9px}
.info__title{font:400 6.3px/1.15 "Open Sans",sans-serif}
.info__text{font:400 4px/1.4 "Open Sans",sans-serif;text-align:justify;margin-top:2px}
.scoop{display:flex;justify-content:center;margin:4px 0 9px}
.scoop svg{display:block}
.compare-band{position:absolute;left:107px;top:290px;width:138px;height:28px;background:var(--green);color:var(--white);
  font:400 3.8px/1.3 "Open Sans",sans-serif;text-align:center;padding:3px 6px}
.maker{position:absolute;left:122px;top:323px;font:400 3.6px/1.35 "Open Sans",sans-serif;color:var(--ink)}
.production-date{position:absolute;left:175px;top:365px;font:700 3.2px/1 "Open Sans",sans-serif;color:var(--ink)}
.production-date__box{width:34px;height:8px;border:1px solid #777;margin-top:2px}
</style>
</head>
<body>
<main class="canvas">

  <section class="pouch pouch--liver" aria-label="Liver chews front">
    <div class="scene" role="img" aria-label="Mountain and forest landscape"></div>
    <div class="pasture" role="img" aria-label="Green pasture with grazing cattle"></div>
    <div class="tab"><div class="tab__title">PREMIUM</div><div class="tab__sub">NATURAL TREATS FOR DOGS</div></div>
    <div class="brand-panel"><span class="brand-panel__dot"></span><span class="brand-panel__name">BARNEY'S<br>SNACKO</span></div>
    <div class="origin-badge" role="img" aria-label="Ethically sourced from New Zealand map seal"></div>
    <div class="dog-photo" role="img" aria-label="Jack Russell terrier portrait"></div>
    <div class="product-name"><div class="product-name__kind">LIVER</div><div class="product-name__type">CHEWS</div><div class="product-name__method">GENTLY AIR DRIED</div></div>
    <div class="divider"></div>
    <div class="window" role="img" aria-label="Clear window showing bone-shaped treats"></div>
    <div class="weight-tag"><div class="weight-tag__label">NET WEIGHT</div><div class="weight-tag__value">150g</div></div>
    <div class="claims"><span class="claims__badge"></span><span class="claims__badge"></span><span class="claims__badge"></span><span class="claims__badge"></span></div>
    <div class="origin-line">NEW ZEALAND PRODUCT</div>
  </section>

  <section class="pouch pouch--heart" aria-label="Heart chews front">
    <div class="scene" role="img" aria-label="Sky with clouds over a field"></div>
    <div class="pasture" role="img" aria-label="Cow standing in green pasture"></div>
    <div class="tab"><div class="tab__title">PREMIUM</div><div class="tab__sub">NATURAL TREATS FOR DOGS</div></div>
    <div class="brand-panel"><span class="brand-panel__dot"></span><span class="brand-panel__name">BARNEY'S<br>SNACKO</span></div>
    <div class="origin-badge" role="img" aria-label="Ethically sourced from New Zealand map seal"></div>
    <div class="dog-photo" role="img" aria-label="Jack Russell terrier portrait"></div>
    <div class="product-name"><div class="product-name__kind">HEART</div><div class="product-name__type">CHEWS</div><div class="product-name__method">GENTLY AIR DRIED</div></div>
    <div class="divider"></div>
    <div class="window" role="img" aria-label="Clear window showing bone-shaped treats"></div>
    <div class="weight-tag"><div class="weight-tag__label">NET WEIGHT</div><div class="weight-tag__value">150g</div></div>
    <div class="claims"><span class="claims__badge"></span><span class="claims__badge"></span><span class="claims__badge"></span><span class="claims__badge"></span></div>
    <div class="origin-line">NEW ZEALAND PRODUCT</div>
  </section>

  <section class="pouch pouch--kidney" aria-label="Kidney chews front">
    <div class="scene" role="img" aria-label="Hills and forest under a blue sky"></div>
    <div class="pasture" role="img" aria-label="Green farmland with cattle"></div>
    <div class="tab"><div class="tab__title">PREMIUM</div><div class="tab__sub">NATURAL TREATS FOR DOGS</div></div>
    <div class="brand-panel"><span class="brand-panel__dot"></span><span class="brand-panel__name">BARNEY'S<br>SNACKO</span></div>
    <div class="origin-badge" role="img" aria-label="Ethically sourced from New Zealand map seal"></div>
    <div class="dog-photo" role="img" aria-label="Jack Russell terrier portrait"></div>
    <div class="product-name"><div class="product-name__kind">KIDNEY</div><div class="product-name__type">CHEWS</div><div class="product-name__method">GENTLY AIR DRIED</div></div>
    <div class="divider"></div>
    <div class="window" role="img" aria-label="Clear window showing bone-shaped treats"></div>
    <div class="weight-tag"><div class="weight-tag__label">NET WEIGHT</div><div class="weight-tag__value">150g</div></div>
    <div class="claims"><span class="claims__badge"></span><span class="claims__badge"></span><span class="claims__badge"></span><span class="claims__badge"></span></div>
    <div class="origin-line">NEW ZEALAND PRODUCT</div>
  </section>

  <section class="pouch pouch--back" aria-label="Pouch back">
    <div class="tab"><div class="tab__title">PREMIUM</div><div class="tab__sub">NATURAL TREATS FOR DOGS</div></div>
    <h2 class="back-heading">TASTE LIFE IN NEW ZEALAND</h2>
    <p class="story-band">Born of love. Crafted for goodness. Made in New Zealand. We are a small team whose love for our dogs is pure and simple, just like our recipes. Hand crafted in small batches every day, we put the best of New Zealand into our authentic farm-to-bowl products so you and your dog can share a lifetime of adventures together.</p>

    <div class="promise-column">
      <div class="promise"><div class="promise__no">-NO-</div><div class="promise__title">Rendered meals</div>
        <p class="promise__text">At Barney's, we never cut corners by using rendered meats or meals. (If you don't know what rendering means, look it up. It's not pretty!) Instead we hand select meats, organs, seafood and bone and bring them together in our family owned facilities in New Zealand, where they are hand-crafted into our air-dried recipes.</p></div>
      <div class="promise"><div class="promise__no">-NO-</div><div class="promise__title">Growth promotants or<br>hormones added</div>
        <p class="promise__text">We believe nature in its simplest form provides an abundance of nutrition. That's why our Barney's meat ingredients are raised without added growth promotants or hormones.</p></div>
      <div class="promise"><div class="promise__no">-NO-</div><div class="promise__title">Grains, rice, soy,<br>potatoes</div>
        <p class="promise__text">A carnivore by nature, your dog is best built to process a whole prey diet, rich in proteins and fats from animal sources. So Barney's never uses grains, corn, soy, potatoes, wheat or rice. Instead our small batch recipes have everything your dog needs to thrive and truly taste life.</p></div>
      <div class="contact">
        <div class="contact__item">barneysnacko.example.com.au</div>
        <div class="contact__item">hello@barneysnacko.example.com.au</div>
        <div class="contact__item">barneysnacko</div>
        <div class="contact__item">#barneysnacko</div>
      </div>
    </div>

    <div class="info-column">
      <div class="info"><div class="info__title">SOURCED FROM ETHICAL<br>NEW ZEALAND FARMS</div>
        <p class="info__text">All of our grass-fed meat, organs and seafood are sourced from ethical and sustainably managed local sources that exceed strict New Zealand standards. From green, free-range farms to the pristine blue waters of our coastline, we put the best of our New Zealand home place into our premium pet foods.</p></div>
      <div class="info"><div class="info__title">NEW ZEALAND GREEN<br>MUSSEL</div>
        <p class="info__text">Did you know that New Zealand Green Mussels are exclusive to our New Zealand homeplace? We include them in our small-batch recipes as a powerhouse superfood, for nutrition you can trust.</p></div>
      <div class="scoop" aria-label="Three scoops equal one">
        <svg width="46" height="9" viewBox="0 0 46 9"><g fill="#222"><path d="M0 1h9l-1 7H1z"/><path d="M11 1h9l-1 7h-7z"/><path d="M22 1h9l-1 7h-7z"/></g><path d="M32.5 3.5h3M32.5 5.5h3" stroke="#222"/><path d="M37 1h9l-1 7h-7z" fill="none" stroke="#222"/></svg>
      </div>
      <div class="info"><div class="info__title">SCOOP SCIENCE</div>
        <p class="info__text">It takes 3 portions of raw ingredients to make 1 portion of Barney's. Our air-drying process preserves the nutrients in our ingredients, while concentrating them into a smaller serving size. This means you feed a smaller quantity in comparison to kibble, raw or canned foods.</p></div>
    </div>
    <p class="compare-band">Our ingredient list is shorter than most, but we don't think you'll miss a thing. Take a look and compare it to our competitors. You'll notice a real difference and we're sure your dog will too.</p>
    <div class="maker">
      Manufactured in New Zealand by:<br>Ltd. 42 Harbour Lane, Rata Bay<br>New Zealand 3199<br>(NZ) 64 7000 1234<br><br>
      Guaranteed in USA by:<br>Inc. Maple Grove,<br>KS 66000 (USA) 1-800-555-0142<br><br>Product of New Zealand
    </div>
    <div class="production-date">DATE OF PRODUCTION<div class="production-date__box"></div></div>
  </section>

</main>
</body>
</html>
```